Cash For clothes textile recycling company leaflet design

We need flyer design for textile recycling company called RK BRIGHTFOLD LTD , we pay cash for peoples unwanted clothes and helping enviroment by moving used unwanted clothing to other countries in need, we are not charity company,as we pay money for people for their unwanted clothing. We would like to see designs that use yellow pink and bright green collors (more summer themes) you can use one or few logos we have uploaded

Industry/Entity Type

Textile

Font styles to use
Decorative

Colors
fbee3d
e34197
33a6d7
abd036
a54499
fece3e

Requirements
Nice to have
• you can play with logos, everything can be colourful, more soft colours, people shouldn't be pushed away from reading the leaflet, some sort of logos with smiles or so can appear as well
Should not have
• no big notes or cash pictures (can be something small) nothing dark or sad looking.

```html
<!DOCTYPE html>
<html lang="en">
<head>
<meta charset="utf-8">
<title>RK Brightfold Ltd – Cash for Clothes Leaflet</title>
<link rel="stylesheet" href="https://fonts.googleapis.com/css2?family=Schoolbell&family=Source+Sans+3:wght@400;700&display=swap">
<style>
  :root {
    --pink: #c9408f;
    --pink-bright: #e34197;
    --pink-soft: #f6dbea;
    --cream: #fbf0c9;
    --yellow: #f1c63a;
    --green: #abd036;
    --blue: #33a6d7;
    --ink: #1c1c1c;
    --paper: #ffffff;
    --backdrop: #efefef;
  }
  * { box-sizing: border-box; margin: 0; padding: 0; }
  html, body {
    width: 1200px; height: 1000px; overflow: hidden;
    background: var(--backdrop);
  }
  .leaflet {
    position: absolute; left: 40px; top: 64px;
    width: 1120px; height: 872px;
    background: var(--paper);
    box-shadow: 0 6px 20px rgba(0,0,0,.18);
    display: flex; flex-direction: column;
    font-family: "Source Sans 3", "Myriad Pro", sans-serif;
    color: var(--ink);
  }
  .leaflet-title {
    font-family: "Schoolbell", cursive;
    color: var(--pink-bright);
    font-size: 50px; font-weight: 400;
    text-transform: uppercase; letter-spacing: 1px;
    text-align: center; line-height: 1; margin-top: 22px;
  }
  .intro {
    font-size: 25px; line-height: 1.22; text-align: center;
    padding: 8px 40px 0;
  }
  .intro strong { font-weight: 700; }
  .figure-row {
    height: 180px; margin: 18px 50px 0;
    background: linear-gradient(90deg, var(--green) 0%, var(--pink-bright) 30%, var(--yellow) 55%, var(--pink-bright) 75%, var(--blue) 100%);
    opacity: .55; border-radius: 8px;
  }
  .rules {
    display: flex; gap: 16px; margin: 18px 30px 0 40px;
  }
  .rule-box { text-align: center; padding: 8px 12px 12px; font-size: 22px; line-height: 1.45; }
  .rule-box h2 {
    font-family: "Schoolbell", cursive; font-weight: 400;
    color: var(--pink); font-size: 36px; line-height: 1;
  }
  .rule-box--accept { background: var(--cream); width: 290px; }
  .rule-box--reject { background: var(--pink-soft); flex: 1; font-size: 21px; }
  .story {
    font-size: 23px; line-height: 1.2; text-align: justify;
    padding: 18px 36px 0 36px;
  }
  .leaflet-footer {
    margin-top: auto; height: 58px; background: var(--pink);
    display: flex; align-items: center; justify-content: space-between;
    padding: 0 60px 0 56px;
    font-family: "Schoolbell", cursive; color: #f7e3ef;
    font-size: 20px; letter-spacing: 2px; text-transform: uppercase;
  }
</style>
</head>
<body>
  <article class="leaflet">
    <h1 class="leaflet-title">We pay cash for your unwanted clothes</h1>
    <p class="intro">We will pay 55p per kg just call <strong>07700900418</strong> or email <strong>hello@rkbrightfold.co.uk</strong> to arrange collection, and our helpful and friendly staff will make sure that your unwanted clothing will be collected as soon as possible, and pay you cash straight away!</p>

    <div class="figure-row" role="img" aria-label="Row of colourful cartoon stick figures in pink, green, yellow and blue holding hands, alternating with small T-shirts"></div>

    <section class="rules">
      <div class="rule-box rule-box--accept">
        <h2>We accept</h2>
        <p>• Any clean dry clothing<br>• Paired shoes • Belts<br>• Handbags</p>
      </div>
      <div class="rule-box rule-box--reject">
        <h2>We do not accept</h2>
        <p>• Bad quality, wet, stained, mouldy or ripped items • Used socks, underwear<br>• Quilts, duvets, pillows • Bedding, curtains • Carpets, mats, rugs • Books<br>• CDs, DVDs, audio and video tapes • Glass, metal, wood</p>
      </div>
    </section>

    <p class="story">For some this industry appears exploitative, but we are incredibly proud of our business's work as textile recyclers. We are not oil companies doing deals with corrupt governments to buy a country's natural resources, nor are we selling old PCs to be dismantled by children breathing in toxic fume; this is a family business doing business with other family businesses to ensure that much-needed clothing can be bought by customers who want it. And we are helping to tackle the problem of what to do with the 900,000 tons of unwanted clothes, which in 2009 the Department of Forestry and Rural Affairs, said went into landfill each year. Things we do will not change the world, but at least it makes a difference. Thank you for reading this, and remember – small things make a big difference!</p>

    <footer class="leaflet-footer">
      <span class="company-name">RK Brightfold Ltd</span>
      <span class="company-reg">Registered in England &amp; Wales</span>
      <span class="company-number">Company number: 08172634</span>
    </footer>
  </article>
</body>
</html>
```